Etiketten-Design für Nahrungsergänzungsmittel
Zielgruppe
Die Firma vertreibt Nahrungsergänzungsmittel, gesunde Lebensmittel, Lifestyle und Wellnessprodukte. Dies vor allem im Fitness und Sport Bereich. Die Marke und das entsprechende Logo sollen auf eine jüngere Zielgruppe 25+ ausgerichtet sein. Personen die für Ihren Körper und Gesundheit Sport treiben und zusätzlich Unterstützung benötigen. Die Produkte werden über Pictoloop durch eine Fitnesstrainerin beworben, und hauptsächlich über Varuno vertrieben. Produkte sind z. B. Produkte zur Ausdauersteigerung, verbesserte Konzentration, Schlaf, Stressbewältigung. Protein Shakes oder Vitamine für Veganer. No gos, Diät Produkte 5kg in 3 Tagen, Potenzsteigerung, Brustvergrößerung oder ähnliches.
Aufgabenstellung
Das Etikett wird auf einen wiederverschließbaren schwarz matten Kraftpapier Beutel im Format 28x20cm aufgebracht. Der Beutel und auch das Etikett sind kompostierbar, sieht aber beides hochwertig aus. Das Produkt ist ein veganes Proteinpulver zum anrühren mit Wasser oder Milchalternative. Einen ersten Entwurf habe ich hochgeladen.

```html
<!DOCTYPE html>
<html lang="de">
<head>
<meta charset="utf-8">
<title>VELIA – Veganer Protein Shake Etikett</title>
<link rel="stylesheet" href="https://fonts.googleapis.com/css2?family=Open+Sans:wght@400;600&family=Quicksand:wght@500&family=Montserrat:wght@800&family=Orbitron:wght@600&family=Saira+Condensed:wght@700&family=Caveat:wght@500&display=swap">
<style>
  :root{
    --bg:#262626;
    --bg-deep:#1e1d1e;
    --divider:#f2f2f2;
    --teal:#17a69a;
    --cream:#f7e6c3;
    --white:#ffffff;
    --ink:#1d1d1d;
    --text:#f4f4f4;
  }
  *{margin:0;padding:0;box-sizing:border-box}
  html,body{width:1200px;height:857px;overflow:hidden;background:var(--bg)}
  .label{position:relative;width:1200px;height:857px;background:var(--bg);font-family:"Open Sans",sans-serif;color:var(--text)}
  .divider{position:absolute;left:597px;top:0;width:5px;height:857px;background:var(--divider)}

  /* front */
  .brand-block{position:absolute;left:113px;top:363px;width:421px;height:117px;background:var(--bg-deep);display:flex;align-items:center;justify-content:center}
  .brand-name{font-family:"Montserrat",sans-serif;font-weight:800;font-size:118px;letter-spacing:4px;color:var(--white);line-height:1}
  .product-title{position:absolute;left:0;width:597px;text-align:center;font-family:"Orbitron",sans-serif;font-weight:600;color:var(--teal);line-height:1}
  .product-title span{position:absolute;left:0;width:100%;font-size:66px;letter-spacing:10px}
  .t1{top:540px}.t2{top:626px}.t3{top:711px}

  /* back */
  .sales-name{position:absolute;left:628px;top:30px;font-size:18.4px;line-height:18px;width:565px}
  .ingredients{position:absolute;left:628px;top:93px;font-size:17.2px;line-height:17.4px;width:480px}
  .section-head{position:absolute;font-family:"Saira Condensed",sans-serif;font-weight:700;font-size:21px;letter-spacing:1.6px;color:var(--white);line-height:1;text-transform:uppercase}
  .section-head.narrow{font-size:19px;letter-spacing:0.4px}

  .cell{position:absolute;color:var(--ink);font-family:"Quicksand",sans-serif;font-weight:500;font-size:13.5px;display:flex;align-items:center}
  .cell.label-cell{padding-left:4px}
  .cell.value{justify-content:center;text-align:center;line-height:14px}
  .cream{background:var(--cream)}
  .plain{background:var(--white)}

  .amino{position:absolute;color:var(--ink);font-family:"Open Sans",sans-serif;font-size:17px;height:20px;display:flex;align-items:center;line-height:1}
  .amino.name{padding-left:4px}
  .amino.val{justify-content:center}

  .usage{position:absolute;left:632px;top:626px;font-size:14.6px;line-height:15.4px;width:184px}
  .greeting{position:absolute;left:856px;top:622px;font-family:"Caveat",cursive;font-size:22px;line-height:27px;color:var(--teal);white-space:nowrap}
  .social{position:absolute;left:859px;top:692px;display:flex;align-items:center;gap:13px}
  .social-dot{width:34px;height:34px;border-radius:50%;background:var(--teal)}
  .social-handle{font-size:21px;color:var(--teal)}
  .company,.contents{position:absolute;top:746px;font-size:16.6px;line-height:17.1px}
  .company{left:628px}
  .contents{left:844px}

  .art{position:absolute;border-radius:6px}
  .art-vanilla{left:1080px;top:126px;width:99px;height:72px;background:linear-gradient(135deg,#6b3b1d,#f8e6b8 55%,#e3b23c)}
  .art-peas{left:1104px;top:222px;width:66px;height:78px;background:radial-gradient(circle,#6fbf3a,#3f8e2a)}
  .art-seed{left:1110px;top:333px;width:54px;height:66px;background:linear-gradient(135deg,#d8c79a,#2f7a34)}
  .art-rice{left:1104px;top:429px;width:66px;height:63px;background:radial-gradient(circle,#f0f0f0,#9a9a9a)}
  .art-person{left:1074px;top:516px;width:120px;height:316px;border-radius:10px;background:linear-gradient(180deg,#d7b38c 0%,#e2bd98 25%,#5d7187 45%,#5d7187 58%,#e2bd98 66%,#1f1f22 74%,#151517 100%)}
</style>
</head>
<body>
<div class="label">

  <section class="front">
    <div class="brand-block"><span class="brand-name">VELIA</span></div>
    <h1 class="product-title">
      <span class="t1">VEGANER</span>
      <span class="t2">PROTEIN</span>
      <span class="t3">SHAKE</span>
    </h1>
  </section>

  <div class="divider"></div>

  <section class="back">
    <p class="sales-name">Getränkepulver zur Herstellung eines veganen Eiweißgetränkes mit Süßungsmittel - Geschmacksrichtung Vanille</p>
    <p class="ingredients">Zutaten: Eiweißmischung (93 %) Erbseneiweiß, Reiseiweiß, Hanfsamenpulver, Bio Kürbiskerneiweiß, Aroma, Verdickungsmittel: Xanthan, Kokosnussmilchpulver, Süßungsmittel: Sucralose</p>

    <div class="art art-vanilla" role="img" aria-label="Illustration einer Vanilleblüte mit Vanilleschoten"></div>
    <div class="art art-peas" role="img" aria-label="Illustration einer Erbsenschote mit Erbsen"></div>
    <div class="art art-seed" role="img" aria-label="Illustration eines Kürbiskerns"></div>
    <div class="art art-rice" role="img" aria-label="Illustration von Reiskörnern"></div>

    <div class="section-head" style="left:628px;top:196px">Nährwertangaben pro</div>
    <div class="section-head narrow" style="left:882px;top:201px">100g</div>
    <div class="section-head narrow" style="left:970px;top:201px">Portion = 30g</div>

    <div class="cell label-cell cream" style="left:628px;top:219px;width:215px;height:30px">Energie</div>
    <div class="cell value cream" style="left:850px;top:219px;width:109px;height:30px">1.9694 kJ<br>401 kcal</div>
    <div class="cell value cream" style="left:965px;top:219px;width:110px;height:30px">1.9694 kJ<br>401 kcal</div>

    <div class="cell label-cell plain" style="left:628px;top:254px;width:215px;height:23px">- davon gesättigte Fettsäuren</div>
    <div class="cell value plain" style="left:850px;top:254px;width:109px;height:23px">8,3 g</div>
    <div class="cell value plain" style="left:965px;top:254px;width:110px;height:23px">8,3 g</div>

    <div class="cell label-cell cream" style="left:628px;top:281px;width:215px;height:23px">Kohlenhydrate</div>
    <div class="cell value cream" style="left:850px;top:281px;width:109px;height:23px">8,3 g</div>
    <div class="cell value cream" style="left:965px;top:281px;width:110px;height:23px">8,3 g</div>

    <div class="cell label-cell plain" style="left:628px;top:308px;width:215px;height:23px">- davon Zucker</div>
    <div class="cell value plain" style="left:850px;top:308px;width:109px;height:23px">8,3 g</div>
    <div class="cell value plain" style="left:965px;top:308px;width:110px;height:23px">8,3 g</div>

    <div class="cell label-cell cream" style="left:628px;top:335px;width:215px;height:23px">Ballaststoffe</div>
    <div class="cell value cream" style="left:850px;top:335px;width:109px;height:23px">8,3 g</div>
    <div class="cell value cream" style="left:965px;top:335px;width:110px;height:23px">8,3 g</div>

    <div class="cell label-cell plain" style="left:628px;top:362px;width:215px;height:23px">Eiweiß</div>
    <div class="cell value plain" style="left:850px;top:362px;width:109px;height:23px">8,3 g</div>
    <div class="cell value plain" style="left:965px;top:362px;width:110px;height:23px">8,3 g</div>

    <div class="cell label-cell cream" style="left:628px;top:389px;width:215px;height:23px">Salz</div>
    <div class="cell value cream" style="left:850px;top:389px;width:109px;height:23px">8,3 g</div>
    <div class="cell value cream" style="left:965px;top:389px;width:110px;height:23px">8,3 g</div>

    <div class="cell label-cell plain" style="left:628px;top:416px;width:215px;height:23px">Fett</div>
    <div class="cell value plain" style="left:850px;top:416px;width:109px;height:23px">8,3 g</div>
    <div class="cell value plain" style="left:965px;top:416px;width:110px;height:23px">8,3 g</div>

    <div class="section-head" style="left:628px;top:453px">Aminosäurenprofil pro 100g Eiweiss</div>

    <div class="amino name cream" style="left:628px;top:477px;width:84px">Eiweiß</div><div class="amino val cream" style="left:714px;top:477px;width:56px">4,4 g</div>
    <div class="amino name cream" style="left:774px;top:477px;width:85px">Eiweiß</div><div class="amino val cream" style="left:862px;top:477px;width:56px">4,4 g</div>
    <div class="amino name cream" style="left:922px;top:477px;width:85px">Eiweiß</div><div class="amino val cream" style="left:1010px;top:477px;width:56px">4,4 g</div>

    <div class="amino name plain" style="left:628px;top:499px;width:84px">Eiweiß</div><div class="amino val plain" style="left:714px;top:499px;width:56px">4,4 g</div>
    <div class="amino name plain" style="left:774px;top:499px;width:85px">Eiweiß</div><div class="amino val plain" style="left:862px;top:499px;width:56px">4,4 g</div>
    <div class="amino name plain" style="left:922px;top:499px;width:85px">Eiweiß</div><div class="amino val plain" style="left:1010px;top:499px;width:56px">4,4 g</div>

    <div class="amino name cream" style="left:628px;top:521px;width:84px">Eiweiß</div><div class="amino val cream" style="left:714px;top:521px;width:56px">4,4 g</div>
    <div class="amino name cream" style="left:774px;top:521px;width:85px">Eiweiß</div><div class="amino val cream" style="left:862px;top:521px;width:56px">4,4 g</div>
    <div class="amino name cream" style="left:922px;top:521px;width:85px">Eiweiß</div><div class="amino val cream" style="left:1010px;top:521px;width:56px">4,4 g</div>

    <div class="amino name plain" style="left:628px;top:543px;width:84px">Eiweiß</div><div class="amino val plain" style="left:714px;top:543px;width:56px">4,4 g</div>
    <div class="amino name plain" style="left:774px;top:543px;width:85px">Eiweiß</div><div class="amino val plain" style="left:862px;top:543px;width:56px">4,4 g</div>
    <div class="amino name plain" style="left:922px;top:543px;width:85px">Eiweiß</div><div class="amino val plain" style="left:1010px;top:543px;width:56px">4,4 g</div>

    <div class="amino name cream" style="left:628px;top:565px;width:84px">Eiweiß</div><div class="amino val cream" style="left:714px;top:565px;width:56px">4,4 g</div>
    <div class="amino name cream" style="left:774px;top:565px;width:85px">Eiweiß</div><div class="amino val cream" style="left:862px;top:565px;width:56px">4,4 g</div>
    <div class="amino name cream" style="left:922px;top:565px;width:85px">Eiweiß</div><div class="amino val cream" style="left:1010px;top:565px;width:56px">4,4 g</div>

    <div class="amino name plain" style="left:628px;top:587px;width:84px">Eiweiß</div><div class="amino val plain" style="left:714px;top:587px;width:56px">4,4 g</div>
    <div class="amino name plain" style="left:774px;top:587px;width:85px">Eiweiß</div><div class="amino val plain" style="left:862px;top:587px;width:56px"></div>
    <div class="amino name plain" style="left:922px;top:587px;width:85px">Eiweiß</div><div class="amino val plain" style="left:1010px;top:587px;width:56px">4,4 g</div>

    <p class="usage">Verzehrempfehlung:<br>30 g Pulver im 300 ml Wasser lösen; Das Produkt ist kühl, trocken und dunkel zu lagern.</p>

    <p class="greeting">Besuche mich auf Pictoloop!<br>liebe Grüße Velia</p>
    <div class="social"><span class="social-dot"></span><span class="social-handle">veliabyvelia</span></div>

    <div class="art art-person" role="img" aria-label="Foto der Fitnesstrainerin mit verschränkten Armen in Sportkleidung"></div>

    <p class="company">VELIA UG<br>Lindenweg 12<br>75000 Musterstadt<br>info@veliabyvelia.de</p>
    <p class="contents">Inhalt: 600 g Eiweißpulver<br>für 20 Shakes<br>Mindestens haltbar bis Ende<br>08/2023; Losnr.: 977109</p>
  </section>

</div>
</body>
</html>
```